Market Research firm needs updated business cards with new logo

We need the logo to be included somewhere on the card (attached). We would also like the phrases "Independent, Objective, Comprehensive" and "Research You Can Trust" somewhere on the card. Front or back. Our colors are hex codes 6075a7, e48d25 and 5a5b5b. Though you are certainly not limited to those shades, whatever you produce should coordinate with them. I have also attached our favicon. Feel free to use it in your design, but please do not use it to replace the full logo.

Contact Information for Business Card

see project description

Font styles to use
Other font styles liked:
• Open Sans

Requirements
Must have
• the logo
• We use Open Sans font

```html
<!DOCTYPE html>
<html lang="en">
<head>
<meta charset="utf-8">
<title>Veridan Research – Business Cards</title>
<link href="https://fonts.googleapis.com/css2?family=Open+Sans:wght@400;600&display=swap" rel="stylesheet">
<style>
  :root {
    --backdrop: #e9e8e6;
    --slate: #7f90a8;
    --orange: #e48d25;
    --ink: #5a5b5b;
    --paper: #ffffff;
    --text-light: #ffffff;
  }
  * { margin: 0; padding: 0; box-sizing: border-box; }
  html, body {
    width: 1200px; height: 715px; overflow: hidden;
    background: var(--backdrop);
    font-family: "Open Sans", Arial, sans-serif;
  }
  .canvas {
    position: relative; width: 1200px; height: 715px;
    display: flex; align-items: center; justify-content: center; gap: 60px;
  }
  .card {
    position: relative; width: 520px; height: 297px;
    border-radius: 3px; overflow: hidden;
    box-shadow: 0 10px 24px rgba(0,0,0,.18);
  }
  /* Front */
  .card-front { background: var(--slate); color: var(--text-light); }
  .card-front .wordmark {
    position: absolute; left: 70px; top: 96px;
    display: flex; align-items: center; gap: 12px;
    font-size: 42px; font-weight: 400; letter-spacing: -0.5px;
  }
  .mark-dot {
    width: 16px; height: 16px; border-radius: 50%;
    background: var(--orange); flex: none;
  }
  .tagline {
    position: absolute; left: 98px; top: 186px;
    font-size: 12.5px; line-height: 1.6; letter-spacing: .3px;
    text-align: center;
  }
  /* Back */
  .card-back { background: var(--slate); }
  .card-back svg.shape { position: absolute; inset: 0; }
  .contact {
    position: absolute; left: 34px; top: 78px; color: var(--text-light);
  }
  .contact .name { font-size: 19px; font-weight: 600; letter-spacing: 1.5px; text-transform: uppercase; }
  .contact .role { font-size: 13px; margin-bottom: 16px; }
  .contact .line { font-size: 12.5px; line-height: 1.55; display: flex; align-items: center; gap: 7px; }
  .contact .line svg { width: 10px; height: 10px; flex: none; }
  .contact .address { font-size: 12.5px; line-height: 1.55; margin-bottom: 2px; }
  .card-back .wordmark {
    position: absolute; right: 30px; top: 100px;
    display: flex; align-items: center; gap: 8px;
    font-size: 28px; font-weight: 400; color: var(--ink); letter-spacing: -0.3px;
    white-space: nowrap;
  }
  .card-back .mark-dot { width: 11px; height: 11px; }
</style>
</head>
<body>
<main class="canvas">
  <section class="card card-front">
    <div class="wordmark"><span class="mark-dot"></span>Veridan Research</div>
    <p class="tagline">Independent - Objective - Comprehensive<br>Research You Can Trust</p>
  </section>

  <section class="card card-back">
    <svg class="shape" viewBox="0 0 520 297" width="520" height="297" aria-hidden="true">
      <path d="M230 0 C175 110 230 240 430 297 L520 297 L520 0 Z" fill="var(--paper)"/>
      <path d="M223 0 C168 110 223 242 420 297" fill="none" stroke="var(--orange)" stroke-width="5"/>
    </svg>
    <div class="contact">
      <div class="name">Daniel Hart</div>
      <div class="role">Director</div>
      <div class="address">2210 Linden Avenue<br>Fairview, VA 22900</div>
      <div class="line">
        <svg viewBox="0 0 10 10"><path d="M2 1 L4 1 L4.6 3 L3.4 3.8 Q4.4 5.8 6.2 6.6 L7 5.4 L9 6 L9 8 Q5 9 2 5.6 Q1 3 2 1Z" fill="#fff"/></svg>
        555 014-2283
      </div>
      <div class="line">
        <svg viewBox="0 0 10 10"><rect x="0.8" y="2" width="8.4" height="6" fill="none" stroke="#fff" stroke-width="1"/><path d="M1 2.3 L5 5.5 L9 2.3" fill="none" stroke="#fff" stroke-width="1"/></svg>
        info@veridanresearch.com
      </div>
      <div class="line">
        <svg viewBox="0 0 10 10"><circle cx="5" cy="5" r="4" fill="none" stroke="#fff" stroke-width="1"/><path d="M1 5 H9 M5 1 Q2.5 5 5 9 M5 1 Q7.5 5 5 9" fill="none" stroke="#fff" stroke-width=".8"/></svg>
        www.veridanresearch.com
      </div>
    </div>
    <div class="wordmark"><span class="mark-dot"></span>Veridan Research</div>
  </section>
</main>
</body>
</html>
```